Wordpress web design

We need a website buil in using Wordpress with 5 pages.

Pages: HOME SERVICES GALLERY TESTIMONIALS CONTACT US ABOUT US.

We are looking for a unique, professional and clean web for our construction company.

Company name: TALL OAK BUILDING SERVICES. We can olso provide you with the logo. Please don't use any flashin, intro, or any ready templates.

All your ideas are welcome.

Many thanks,
Dorian

Target Market(s)

Construction

Industry/Entity Type

Construction

Font styles to use
Sans Serif
Decorative

Requirements
Must have
• Connect with construction and London
Nice to have
• Nice and clean

```html
<!DOCTYPE html>
<html lang="en">
<head>
<meta charset="utf-8">
<title>Contact Us – Tall Oak Building Services</title>
<link href="https://fonts.googleapis.com/css2?family=Rokkitt:wght@400;700&family=Arvo:wght@400;700&display=swap" rel="stylesheet">
<style>
  :root {
    --backdrop: #e6dfd6;
    --backdrop-stripe: #ddd5cb;
    --page: #ffffff;
    --ink: #444444;
    --ink-strong: #1e1e1e;
    --green: #2a8a0e;
    --green-dark: #1a5a08;
    --green-mid: #2a7d10;
    --rule: #dddddd;
    --panel: #efefef;
    --panel-border: #cfcfcf;
    --link: #1a1aff;
    --map-sea: #a9c6ec;
    --map-land: #e8e4d8;
  }
  * { box-sizing: border-box; margin: 0; padding: 0; }
  html, body { width: 1200px; height: 822px; overflow: hidden; }
  body {
    background: repeating-linear-gradient(90deg, var(--backdrop) 0 18px, var(--backdrop-stripe) 18px 20px);
    font-family: "Rokkitt", serif;
    color: var(--ink);
    position: relative;
  }
  .page {
    position: absolute; left: 120px; top: 0; width: 952px; height: 822px;
    background: var(--page);
    box-shadow: 0 0 8px rgba(0,0,0,.25);
  }
  .main-nav {
    position: absolute; left: 20px; top: 22px; width: 913px; height: 41px;
    border-top: 1px dashed var(--rule); border-bottom: 1px dashed var(--rule);
    display: flex; align-items: center; padding-left: 0;
  }
  .main-nav a {
    font-family: "Arvo", serif; font-size: 14px; color: #555; text-decoration: none;
    height: 34px; line-height: 34px; padding: 0 18px; position: relative;
  }
  .main-nav a + a::before {
    content: ""; position: absolute; left: 0; top: 9px; height: 16px; border-left: 1px solid var(--rule);
  }
  .main-nav a.is-current { background: var(--green); color: #fff; margin: 0 6px; }
  .main-nav a.is-current::before, .main-nav a.is-current + a::before { display: none; }

  .page-title {
    position: absolute; left: 20px; top: 99px; width: 913px; height: 42px;
    border: 1px solid var(--panel-border); padding: 3px;
  }
  .page-title h1 {
    background: var(--panel); height: 100%; font-weight: 400; font-size: 20px;
    font-family: "Rokkitt", serif; color: #333; padding-left: 10px; line-height: 34px;
  }
  .intro { position: absolute; left: 20px; top: 183px; font-size: 14px; font-weight: 700; font-family: "Arvo", serif; color: #555; }

  .contact-form { position: absolute; left: 20px; top: 250px; width: 290px; font-size: 16px; }
  .contact-form label { display: block; margin-bottom: 1px; }
  .contact-form input { display: block; width: 286px; height: 18px; border: 1px solid #888; margin-bottom: 22px; }
  .contact-form textarea { display: block; width: 284px; height: 159px; border: 1px solid #888; resize: none; }
  .contact-form button {
    margin-top: 23px; width: 50px; height: 17px; font-size: 12px; font-family: "Arvo", serif;
    border: 1px solid #999; background: linear-gradient(#f6f6f6, #dcdcdc); color: #222;
  }

  .company-card { position: absolute; left: 350px; top: 216px; font-size: 15.5px; line-height: 19px; font-style: normal; }
  .company-card strong { color: var(--ink-strong); font-family: "Arvo", serif; font-size: 13px; }
  .company-card a { color: var(--link); text-decoration: none; }
  .location-map {
    position: absolute; left: 350px; top: 346px; width: 288px; height: 287px;
    background: linear-gradient(180deg, var(--map-land) 0 25%, var(--map-sea) 45%, var(--map-sea) 70%, var(--map-land) 100%);
  }

  .site-footer {
    position: absolute; left: 0; top: 730px; width: 952px; height: 92px;
    background: linear-gradient(90deg, var(--green-dark), var(--green-mid) 45%, var(--green-dark));
  }
  .footer-widget { position: absolute; top: 28px; }
  .footer-widget h2 {
    font-family: "Arvo", serif; font-weight: 400; font-size: 19px; color: #fff;
    padding-bottom: 10px; border-bottom: 1px dotted rgba(255,255,255,.35); width: 211px;
  }
  .search-box { position: absolute; left: 721px; top: 26px; width: 177px; height: 28px; display: flex; border: 1px solid #3a7a26; }
  .search-box span { flex: 1; background: #164c06; color: #fff; font: 700 12px "Arvo", serif; padding: 7px 8px; }
  .search-box i { width: 36px; background: #0f3a04; display: flex; align-items: center; justify-content: center; }
</style>
</head>
<body>
  <div class="page">
    <nav class="main-nav">
      <a href="#">Home</a>
      <a href="#">SERVICES</a>
      <a href="#">GALLERY</a>
      <a href="#">TESTIMONIALS</a>
      <a href="#" class="is-current">CONTACT US</a>
      <a href="#">ABOUT US</a>
    </nav>

    <div class="page-title"><h1>CONTACT US &nbsp;»</h1></div>

    <p class="intro">You can send a message .</p>

    <form class="contact-form">
      <label>Your Name (required)</label>
      <input type="text">
      <label>Your Email (required)</label>
      <input type="email">
      <label>Your Message</label>
      <textarea></textarea>
      <button type="button">SEND</button>
    </form>

    <address class="company-card">
      <strong>TALL OAK BUILDING SERVICES</strong><br>
      18 Hadley Court<br>
      7 Marlow Square<br>
      London E9 2QT<br>
      <a href="#">hello@talloakbuild.example</a>
    </address>

    <div class="location-map" role="img" aria-label="Map showing the company location in south-east England"></div>

    <footer class="site-footer">
      <div class="footer-widget" style="left:20px"><h2>Adout Company</h2></div>
      <div class="footer-widget" style="left:260px"><h2>Archives Widget</h2></div>
      <div class="footer-widget" style="left:491px"><h2>Categories</h2></div>
      <div class="search-box">
        <span>Search</span>
        <i><svg width="14" height="14" viewBox="0 0 14 14"><circle cx="5.5" cy="5.5" r="4" fill="none" stroke="#cfe8c4" stroke-width="2"/><line x1="8.5" y1="8.5" x2="13" y2="13" stroke="#cfe8c4" stroke-width="2.4"/></svg></i>
      </div>
    </footer>
  </div>
</body>
</html>
```